Ceiling fan flyer design

We are after a double sided flyer design offering ceiling fan installations

Target Market(s)

Home owners

Requirements
Must have
• content listed

```html
<!DOCTYPE html>
<html lang="en">
<head>
<meta charset="utf-8">
<title>Ceiling Fan Installation Flyer</title>
<link rel="stylesheet" href="https://fonts.googleapis.com/css2?family=Arimo:ital,wght@0,400;0,700;1,400&family=Roboto+Condensed:wght@700&display=swap">
<style>
:root{
  --sky-dark:#0f5fa8;
  --sky-mid:#2f8fd6;
  --sky-light:#8fd0f5;
  --orange:#f7941d;
  --orange-dark:#e06a10;
  --call-red:#c0272d;
  --green:#3aa14a;
  --green-dark:#1f7a32;
  --strip:#165c2a;
  --yellow:#ffe14d;
  --red:#e2262b;
  --red-dark:#b3161c;
  --blue-box:#1d64b3;
  --blue-text:#1b5fad;
  --ink:#333;
  --footer:#dce6f0;
  --white:#fff;
}
*{box-sizing:border-box;margin:0;padding:0}
html,body{width:870px;height:1200px;overflow:hidden}
body{font-family:"Arimo",Arial,sans-serif;background:var(--white);color:var(--ink)}
.flyer{position:relative;width:870px;height:1200px;overflow:hidden;background:var(--white)}

.hero{position:absolute;left:0;top:0;width:870px;height:480px;
  background:radial-gradient(ellipse at 65% 35%,var(--sky-light) 0%,var(--sky-mid) 45%,var(--sky-dark) 100%)}
.brand{position:absolute;left:34px;top:40px;display:flex;align-items:center;gap:14px}
.brand-dot{width:46px;height:46px;border-radius:50%;background:var(--orange)}
.brand-name{font-weight:700;font-size:30px;color:var(--white);line-height:1.1;width:230px}
.mascot-area{position:absolute;left:40px;top:150px;width:260px;height:250px;border-radius:16px;
  background:linear-gradient(160deg,#f3c27a,#c8402f)}
.fan-area{position:absolute;left:360px;top:40px;width:480px;height:240px;border-radius:20px;
  background:radial-gradient(ellipse at center,#7a5a3c 0%,#5a3f28 35%,rgba(90,63,40,0) 72%)}
.call-box{position:absolute;left:580px;top:300px;width:260px;border-radius:10px;overflow:hidden;
  box-shadow:0 4px 10px rgba(0,0,0,.3)}
.call-label{background:linear-gradient(var(--orange),var(--orange-dark));color:var(--white);
  font-family:"Roboto Condensed","Arial Narrow",sans-serif;font-weight:700;font-size:34px;text-align:center;padding:8px 0 6px}
.call-number{background:var(--white);color:var(--call-red);font-family:"Roboto Condensed","Arial Narrow",sans-serif;
  font-weight:700;font-size:42px;text-align:center;padding:8px 0}

.headline-band{position:absolute;left:0;top:480px;width:870px;height:200px;
  background:linear-gradient(var(--green),var(--green-dark));color:var(--white);padding:22px 36px}
.headline{font-size:58px;font-weight:700;letter-spacing:-1px;line-height:1}
.subhead{font-size:30px;font-weight:700;margin-top:20px}
.intro{font-size:18px;line-height:1.35;margin-top:8px;max-width:780px}

.web-strip{position:absolute;left:0;top:680px;width:870px;height:44px;background:var(--strip);
  color:var(--yellow);font-family:"Roboto Condensed","Arial Narrow",sans-serif;font-weight:700;font-size:26px;padding:6px 36px;letter-spacing:.5px}

.offer{position:absolute;left:30px;top:748px;width:390px;height:150px;border-radius:10px;
  background:linear-gradient(var(--red),var(--red-dark));color:var(--white);
  font-family:"Roboto Condensed","Arial Narrow",sans-serif;font-weight:700;font-size:44px;line-height:1.15;
  text-align:center;display:flex;align-items:center;justify-content:center}
.testimonials{position:absolute;left:30px;top:912px;width:390px;height:170px;border-radius:10px;
  background:var(--blue-box);color:var(--white);padding:14px 18px}
.quote{font-style:italic;font-size:15px;line-height:1.3}
.quote-by{font-weight:700;font-size:14px;text-align:right;margin:4px 0 12px}

.guarantee{position:absolute;left:450px;top:744px;width:390px}
.guarantee h2{color:var(--blue-text);font-size:32px;font-weight:700;margin-bottom:10px}
.guarantee ul{list-style:none}
.guarantee li{position:relative;padding-left:22px;font-size:16px;line-height:1.3;margin-bottom:7px}
.guarantee li::before{content:"";position:absolute;left:2px;top:6px;width:9px;height:9px;background:var(--blue-text)}

.footer{position:absolute;left:0;top:1096px;width:870px;height:104px;background:var(--footer);
  display:flex;align-items:center;padding:0 30px;gap:22px}
.cards{display:flex;gap:8px}
.card{width:60px;height:40px;border-radius:4px;background:#9aa9ba}
.conditions{color:var(--blue-text);font-size:16px;line-height:1.35}
.conditions strong{font-weight:700}
</style>
</head>
<body>
<div class="flyer">
  <section class="hero">
    <div class="brand">
      <span class="brand-dot"></span>
      <span class="brand-name">Spark Ready Electrical</span>
    </div>
    <div class="mascot-area" role="img" aria-label="Cartoon electrician superhero holding a light bulb"></div>
    <div class="fan-area" role="img" aria-label="Wooden ceiling fan with five blades"></div>
    <div class="call-box">
      <div class="call-label">Call Us</div>
      <div class="call-number">1300 472 618</div>
    </div>
  </section>

  <section class="headline-band">
    <h1 class="headline">Hot sweaty Uncomfortable</h1>
    <p class="subhead">A breeze without the cost!</p>
    <p class="intro">Enjoy the gentle breeze &amp; cooling effect of a ceiling fan to help you sleep soundly at night &amp; be more productive during the day.</p>
  </section>

  <div class="web-strip">www.sparkreadyelectrical.com.au</div>

  <div class="offer"><p>Save $25 OFF every<br>2nd fan installed</p></div>

  <section class="testimonials">
    <p class="quote">"We can now sleep! Wow what a difference! Thanks Marcus for your help."</p>
    <p class="quote-by">Gregor &amp; Lena Hartfield</p>
    <p class="quote">"Super service! What a pleasant change. Marcus could not have done more to ensure our satisfaction."</p>
    <p class="quote-by">Dom &amp; Rosa, Ashvale</p>
  </section>

  <section class="guarantee">
    <h2>We guarantee to:</h2>
    <ul>
      <li>Always be on time, or we pay you $100</li>
      <li>Tell you the exact cost before any job begins</li>
      <li>Provide you with a fixed price guarantee, assuring you have no extra costs</li>
      <li>Leave your place as clean as it was when we first arrived</li>
      <li>Return, and fix it for free, if it's not right</li>
      <li>Return your telephone calls promptly</li>
      <li>Provide a minimum 12 Month warranty on all parts</li>
      <li>Provide friendly, helpful service and advice</li>
    </ul>
  </section>

  <footer class="footer">
    <div class="cards">
      <span class="card"></span><span class="card"></span><span class="card"></span>
    </div>
    <p class="conditions"><strong>CONDITIONS:</strong> Mention this ad when booking to receive offer.<br>Limit one per household. Cannot be combined with any other offer.</p>
  </footer>
</div>
</body>
</html>
```